Slow Harbour Airs. A CD of beautiful 17th century music for lute played by a world famous lutenist.

Hi designers,
My name is Toby Kellerman and I am an international lute player in need of a CD cover design. I am blind, so will be relying on other people's eyes and descriptions during the process, including yours! Are you up for the challenge?
My CD is called Slow Harbour Airs. It's beautiful lute music from the 17th century, very intimate and carming, but also very powerful.
I would like you to use the attached image, and find a way to include the following text in a tasteful way:
The text for the front cover is as follows:
Slow Harbour Airs
Tobias Kellerman - lute and theorbo
Music by Fenwright, Halbrook, Pilcher, Brandt, Lombretti and Ostenfeld.
Here is a cliphaven link to some of the music I play, which should give you an idea:
www.cliphaven.com/tobykellerman7
Here is a link to my website, where you can see the covers of my other CDs, and get more information about me:
www.tobiaskellerman.net
I'm excited to receive your design and ideas.
Best wishes
Toby

```html
<!DOCTYPE html>
<html lang="en">
<head>
<meta charset="utf-8">
<title>Slow Harbour Airs – Tobias Kellerman</title>
<link rel="stylesheet" href="https://fonts.googleapis.com/css2?family=Playfair+Display:wght@500&family=Michroma&display=swap">
<style>
  :root {
    --ink-dark: #141212;
    --umber: #3a2a1f;
    --amber: #a8773f;
    --lamp: #e9dcc4;
    --panel-grey: rgba(128, 128, 128, 0.55);
    --panel-band: rgba(12, 12, 12, 0.82);
    --panel-credits: rgba(150, 150, 150, 0.6);
    --text-light: #ffffff;
  }
  html, body {
    margin: 0;
    padding: 0;
    width: 1200px;
    height: 1200px;
    overflow: hidden;
    background: var(--ink-dark);
  }
  .cover {
    position: relative;
    width: 1200px;
    height: 1200px;
    overflow: hidden;
  }
  .cover-art {
    position: absolute;
    inset: 0;
    background:
      radial-gradient(circle at 82% 28%, var(--lamp) 0, rgba(233,220,196,0.5) 5%, transparent 14%),
      radial-gradient(ellipse at 38% 68%, #d9a86a 0, var(--amber) 18%, transparent 38%),
      radial-gradient(ellipse at 60% 30%, #6b4a2e 0, transparent 45%),
      linear-gradient(160deg, #2a1f19 0%, var(--umber) 45%, #1a1614 100%);
  }
  .title-panel {
    position: absolute;
    left: 636px;
    top: 0;
    width: 564px;
    height: 775px;
    background: var(--panel-grey);
  }
  .album-title {
    position: absolute;
    left: 636px;
    top: 40px;
    width: 564px;
    margin: 0;
    display: flex;
    flex-direction: column;
    align-items: center;
    font-family: "Playfair Display", serif;
    font-weight: 500;
    font-size: 205px;
    line-height: 228px;
    color: var(--text-light);
    text-shadow: 0 2px 6px rgba(0,0,0,0.35);
  }
  .album-title span {
    display: block;
    white-space: nowrap;
    transform: scaleX(0.6);
    transform-origin: center;
  }
  .artist-band {
    position: absolute;
    left: 636px;
    top: 775px;
    width: 564px;
    height: 160px;
    background: var(--panel-band);
    display: flex;
    flex-direction: column;
    justify-content: center;
    align-items: center;
    gap: 10px;
  }
  .artist-band p {
    margin: 0;
    font-family: "Michroma", sans-serif;
    font-size: 26px;
    letter-spacing: 3px;
    color: var(--text-light);
    text-transform: uppercase;
  }
  .credits-panel {
    position: absolute;
    left: 636px;
    top: 950px;
    width: 550px;
    height: 140px;
    background: var(--panel-credits);
    display: flex;
    flex-direction: column;
    justify-content: center;
    align-items: center;
    gap: 4px;
  }
  .credits-panel p {
    margin: 0;
    font-family: "Michroma", sans-serif;
    font-size: 19px;
    letter-spacing: 1.5px;
    color: var(--text-light);
    text-transform: uppercase;
    white-space: nowrap;
  }
</style>
</head>
<body>
  <main class="cover">
    <div class="cover-art" role="img" aria-label="Painting of a lute leaning against a table in a candlelit tavern, warm amber and umber brushwork"></div>
    <div class="title-panel"></div>
    <h1 class="album-title"><span>Slow</span><span>Harbour</span><span>Airs</span></h1>
    <div class="artist-band">
      <p>Tobias Kellerman</p>
      <p>Lute and Theorbo</p>
    </div>
    <div class="credits-panel">
      <p>Music by:</p>
      <p>Fenwright &bull; Halbrook &bull; Pilcher</p>
      <p>Brandt &bull; Lombretti &bull; Ostenfeld</p>
    </div>
  </main>
</body>
</html>
```